Business card for a business coach / management consultant

My logo has been done and now I need a business card. Deliverable needs to be a PDF to give to the printer. I want it single sided as I want the back side blank.
I prefer a white card with modern simple professional design.
Details are:
Tobias Wrenfield
B.Sc. (hons) FRTB CP MEGOL
14 Calloway Rd
Larkhaven WA 6077
Australia
mobile 041 23 584 17
email tobias@corporatepathlane.com.au
skype tobiaswrenfield8
Small to medium size business owners
Business

```html
<!DOCTYPE html>
<html lang="en">
<head>
<meta charset="utf-8">
<title>Corporate Pathlane – Business Card Concepts</title>
<link href="https://fonts.googleapis.com/css2?family=Arimo:wght@400;700&family=Didact+Gothic&display=swap" rel="stylesheet">
<style>
  :root{
    --brand-blue:#0a2a9e;
    --text-grey:#5a6670;
    --border:#222;
    --paper:#ffffff;
  }
  *{box-sizing:border-box;margin:0;padding:0}
  html,body{width:1200px;height:1000px;overflow:hidden;background:var(--paper)}
  body{position:relative;font-family:"Didact Gothic",Arial,sans-serif}

  .concept-label{position:absolute;font-family:Arimo,Arial,sans-serif;font-size:19px;color:#111;transform:translateX(-50%)}

  .card{position:absolute;width:386px;height:211px;border:1px solid var(--border);background:var(--paper);overflow:hidden}
  .card--portrait{width:212px;height:386px}

  /* logo stand-in */
  .logo{position:absolute;display:flex;flex-direction:column;align-items:center;transform:translateX(-50%)}
  .logo__dot{width:24px;height:24px;border-radius:50%;background:var(--brand-blue);margin-bottom:4px}
  .logo__name{font-family:Arimo,Arial,sans-serif;font-weight:700;color:var(--brand-blue);font-size:13px;line-height:13px;text-align:center}
  .logo--large .logo__dot{width:36px;height:36px;margin-bottom:6px}
  .logo--large .logo__name{font-size:18px;line-height:18px}

  /* name */
  .holder{position:absolute;white-space:nowrap}
  .holder__name{font-family:Arimo,Arial,sans-serif;font-weight:700;font-size:18px;color:var(--brand-blue);line-height:21px}
  .holder__creds{font-size:9.5px;color:var(--text-grey);line-height:12px}
  .holder--center{transform:translateX(-50%);text-align:center}
  .holder--right{text-align:right}
  .holder--pill{background:var(--brand-blue);padding:4px 10px 4px 13px}
  .holder--pill .holder__name,.holder--pill .holder__creds{color:#fff}
  .holder--pill .holder__name{font-size:17px;line-height:20px}
  .holder--pill-right{border-radius:0 12px 12px 0}
  .holder--pill-left{border-radius:12px 0 0 12px;right:0;padding-right:8px}

  /* details */
  .address,.contacts{position:absolute;font-size:10px;line-height:12.5px;color:var(--text-grey);white-space:nowrap}
  .address--right{text-align:right}
  .address--center{transform:translateX(-50%);text-align:center}
  .contacts{text-align:right}
  .contacts li{list-style:none;display:flex;justify-content:flex-end;align-items:center;gap:1px}
  .icon{width:8px;height:8px;flex:none;color:var(--brand-blue)}
</style>
</head>
<body>

<svg width="0" height="0" style="position:absolute">
  <symbol id="i-phone" viewBox="0 0 8 8"><rect x="2" y="0" width="4" height="8" rx="1" fill="currentColor"/><rect x="2.8" y="1" width="2.4" height="5" fill="#fff"/></symbol>
  <symbol id="i-chat" viewBox="0 0 8 8"><circle cx="4" cy="4" r="3.2" fill="currentColor"/></symbol>
  <symbol id="i-mail" viewBox="0 0 8 8"><rect x="0.5" y="1.5" width="7" height="5" fill="none" stroke="currentColor"/><path d="M0.5 1.5 L4 4.5 L7.5 1.5" fill="none" stroke="currentColor"/></symbol>
</svg>

<!-- 1 -->
<span class="concept-label" style="left:178px;top:35px">1</span>
<section class="card" style="left:3px;top:59px">
  <div class="logo" style="left:321px;top:14px"><span class="logo__dot"></span><span class="logo__name">Corporate<br>Pathlane</span></div>
  <div class="holder holder--center" style="left:175px;top:91px"><p class="holder__name">Tobias Wrenfield</p><p class="holder__creds">B.Sc. (hons) FRTB CP MEGOL</p></div>
  <p class="address" style="left:15px;top:152px">14 Calloway Rd<br>Larkhaven WA 6077<br>Australia</p>
  <ul class="contacts" style="right:27px;top:152px">
    <li><svg class="icon"><use href="#i-phone"/></svg>: 041 23 584 17</li>
    <li><svg class="icon"><use href="#i-chat"/></svg>: tobiaswrenfield8</li>
    <li><svg class="icon"><use href="#i-mail"/></svg>:tobias@corporatepathlane.com.au</li>
  </ul>
</section>

<!-- 2 -->
<span class="concept-label" style="left:194px;top:395px">2</span>
<section class="card" style="left:0;top:430px">
  <div class="logo" style="left:321px;top:14px"><span class="logo__dot"></span><span class="logo__name">Corporate<br>Pathlane</span></div>
  <div class="holder" style="left:15px;top:107px"><p class="holder__name">Tobias Wrenfield</p><p class="holder__creds">B.Sc. (hons) FRTB CP MEGOL</p></div>
  <p class="address" style="left:15px;top:152px">14 Calloway Rd<br>Larkhaven WA 6077<br>Australia</p>
  <ul class="contacts" style="right:27px;top:152px">
    <li><svg class="icon"><use href="#i-phone"/></svg>: 041 23 584 17</li>
    <li><svg class="icon"><use href="#i-chat"/></svg>: tobiaswrenfield8</li>
    <li><svg class="icon"><use href="#i-mail"/></svg>:tobias@corporatepathlane.com.au</li>
  </ul>
</section>

<!-- 3 -->
<span class="concept-label" style="left:194px;top:735px">3</span>
<section class="card" style="left:0;top:766px">
  <div class="logo" style="left:321px;top:16px"><span class="logo__dot"></span><span class="logo__name">Corporate<br>Pathlane</span></div>
  <div class="holder" style="left:13px;top:52px"><p class="holder__name">Tobias Wrenfield</p><p class="holder__creds">B.Sc. (hons) FRTB CP MEGOL</p></div>
  <p class="address" style="left:15px;top:153px">14 Calloway Rd<br>Larkhaven WA 6077<br>Australia</p>
  <ul class="contacts" style="right:27px;top:153px">
    <li><svg class="icon"><use href="#i-phone"/></svg>: 041 23 584 17</li>
    <li><svg class="icon"><use href="#i-chat"/></svg>: tobiaswrenfield8</li>
    <li><svg class="icon"><use href="#i-mail"/></svg>:tobias@corporatepathlane.com.au</li>
  </ul>
</section>

<!-- 4 -->
<span class="concept-label" style="left:600px;top:25px">4</span>
<section class="card card--portrait" style="left:495px;top:52px">
  <div class="logo logo--large" style="left:106px;top:72px"><span class="logo__dot"></span><span class="logo__name">Corporate<br>Pathlane</span></div>
  <div class="holder holder--pill holder--pill-left" style="top:236px"><p class="holder__name">Tobias Wrenfield</p><p class="holder__creds">B.Sc. (hons) FRTB CP MEGOL</p></div>
  <p class="address address--right" style="right:15px;top:294px">14 Calloway Rd<br>Larkhaven WA 6077<br>Australia</p>
  <ul class="contacts" style="right:15px;top:336px">
    <li><svg class="icon"><use href="#i-phone"/></svg>: 041 23 584 17</li>
    <li><svg class="icon"><use href="#i-chat"/></svg>: tobiaswrenfield8</li>
    <li><svg class="icon"><use href="#i-mail"/></svg>:tobias@corporatepathlane.com.au</li>
  </ul>
</section>

<!-- 5 -->
<span class="concept-label" style="left:600px;top:508px">5</span>
<section class="card" style="left:407px;top:549px">
  <div class="logo" style="left:194px;top:28px"><span class="logo__dot"></span><span class="logo__name">Corporate<br>Pathlane</span></div>
  <div class="holder holder--center" style="left:194px;top:95px"><p class="holder__name">Tobias Wrenfield</p><p class="holder__creds">B.Sc. (hons) FRTB CP MEGOL</p></div>
  <p class="address" style="left:15px;top:153px">14 Calloway Rd<br>Larkhaven WA 6077<br>Australia</p>
  <ul class="contacts" style="right:27px;top:153px">
    <li><svg class="icon"><use href="#i-phone"/></svg>: 041 23 584 17</li>
    <li><svg class="icon"><use href="#i-chat"/></svg>: tobiaswrenfield8</li>
    <li><svg class="icon"><use href="#i-mail"/></svg>:tobias@corporatepathlane.com.au</li>
  </ul>
</section>

<!-- 6 -->
<span class="concept-label" style="left:1018px;top:21px">6</span>
<section class="card" style="left:810px;top:58px">
  <div class="logo" style="left:321px;top:16px"><span class="logo__dot"></span><span class="logo__name">Corporate<br>Pathlane</span></div>
  <div class="holder holder--pill holder--pill-right" style="left:0;top:106px"><p class="holder__name">Tobias Wrenfield</p><p class="holder__creds">B.Sc. (hons) FRTB CP MEGOL</p></div>
  <p class="address" style="left:15px;top:153px">14 Calloway Rd<br>Larkhaven WA 6077<br>Australia</p>
  <ul class="contacts" style="right:28px;top:152px">
    <li><svg class="icon"><use href="#i-phone"/></svg>: 041 23 584 17</li>
    <li><svg class="icon"><use href="#i-chat"/></svg>: tobiaswrenfield8</li>
    <li><svg class="icon"><use href="#i-mail"/></svg>:tobias@corporatepathlane.com.au</li>
  </ul>
</section>

<!-- 7 -->
<span class="concept-label" style="left:1015px;top:401px">7</span>
<section class="card" style="left:810px;top:439px">
  <div class="logo" style="left:56px;top:22px"><span class="logo__dot"></span><span class="logo__name">Corporate<br>Pathlane</span></div>
  <div class="holder holder--right" style="right:26px;top:101px"><p class="holder__name">Tobias Wrenfield</p><p class="holder__creds">B.Sc. (hons) FRTB CP MEGOL</p></div>
  <p class="address" style="left:17px;top:157px">14 Calloway Rd<br>Larkhaven WA 6077<br>Australia</p>
  <ul class="contacts" style="right:28px;top:152px">
    <li><svg class="icon"><use href="#i-phone"/></svg>: 041 23 584 17</li>
    <li><svg class="icon"><use href="#i-chat"/></svg>: tobiaswrenfield8</li>
    <li><svg class="icon"><use href="#i-mail"/></svg>:tobias@corporatepathlane.com.au</li>
  </ul>
</section>

<!-- 8 -->
<span class="concept-label" style="left:1015px;top:716px">8</span>
<section class="card" style="left:812px;top:765px">
  <div class="logo" style="left:60px;top:18px"><span class="logo__dot"></span><span class="logo__name">Corporate<br>Pathlane</span></div>
  <div class="holder holder--center" style="left:189px;top:84px"><p class="holder__name">Tobias Wrenfield</p><p class="holder__creds">B.Sc. (hons) FRTB CP MEGOL</p></div>
  <p class="address address--center" style="left:189px;top:124px">14 Calloway Rd<br>Larkhaven WA 6077<br>Australia</p>
  <ul class="contacts" style="right:30px;top:161px">
    <li><svg class="icon"><use href="#i-phone"/></svg>: 041 23 584 17</li>
    <li><svg class="icon"><use href="#i-chat"/></svg>: tobiaswrenfield8</li>
    <li><svg class="icon"><use href="#i-mail"/></svg>:tobias@corporatepathlane.com.au</li>
  </ul>
</section>

</body>
</html>
```